Real Estate Team Business Card

We need a business card designed for our real estate team called "Larkspur Realty Group". We would like to receive a final format that would allow us to edit the contact information for new employees as they are added to our team. The difficult part of the design is that we will need to have two logos on the card - both our team name logo for "Larkspur Realty Group" and our company logo for "Corvane Real Estate". Most emphasis should be given to the team logo - maybe double the size of our company logo. (we just have to have the company logo somewhere on the card for legal purposes) The design should somehow illustrate we work in real estate, but still use the beehive/bee concept as a lot of our marketing will involve "bee" sayings. We would also like to use the tagline: "find out what all the buzz is about". We also need to use the "fair housing" logo and "realtor" logos. These can both be small like the company logo.
Target Market(s)
Real Estate
Industry/Entity Type
Real Estate Agent
Contact Information for Business Card
Name: Dylan Marsh Title: Realtor Phone: 801-555-0172 Email: dylan@larkspurrealtrygroup.com Website: www.larkspurrealtygroup.com Facebook: fb/me/larkspurrealtygroup Twitter: @LarkspurRltyGrp
Colors
Designer to choose colors to be used in the design.
Requirements
Must have
- Contact information. Larkspur Realty Group Logo. Corvane Real Estate Logo. Realtor logo. Fair Housing Logo. Tagline: "find out what all the buzz is about".
Nice to have
- It would be nice to illustrate that we work in real estate. It would also be nice to somehow incorporate bees or play off of our beehive logo. We will do a lot of marking using sayings like "let us bee the solution" or "real estate meant to bee" etc.

```html
<!DOCTYPE html>
<html lang="en">
<head>
<meta charset="utf-8">
<title>Larkspur Realty Group – Business Card</title>
<link href="https://fonts.googleapis.com/css2?family=Roboto:wght@400;700&family=Raleway:wght@400;500&display=swap" rel="stylesheet">
<style>
  :root {
    --backdrop: #6e5038;
    --card-white: #ffffff;
    --card-black: #000000;
    --honey: #f7c600;
    --ink: #1a1a1a;
    --corvane-blue: #0a4f9c;
    --divider: #c9c9c9;
  }
  * { margin: 0; padding: 0; box-sizing: border-box; }
  html, body { width: 1125px; height: 1200px; overflow: hidden; }
  body {
    position: relative;
    background: var(--backdrop);
    font-family: "Roboto", Arial, sans-serif;
  }
  .card {
    position: absolute;
    left: 171px;
    width: 826px;
    height: 472px;
    box-shadow: 0 4px 10px rgba(0,0,0,0.45);
    overflow: hidden;
  }
  .card--front { top: 106px; background: var(--card-white); }
  .card--back  { top: 639px; background: var(--card-black); }

  /* Front */
  .company-mark {
    position: absolute;
    right: 48px;
    top: 36px;
    color: var(--corvane-blue);
    font-family: "Roboto", Arial, sans-serif;
    font-weight: 400;
    font-size: 17px;
    line-height: 1.1;
    text-align: right;
  }
  .team-mark {
    position: absolute;
    left: 52px;
    top: 262px;
    width: 300px;
    text-align: center;
    color: var(--ink);
    font-family: "Roboto", Arial, sans-serif;
    font-weight: 400;
  }
  .team-mark__name { display: block; font-size: 36px; letter-spacing: 5px; line-height: 1; }
  .team-mark__sub  { display: block; font-size: 13px; letter-spacing: 4px; margin-top: 10px; }
  .divider {
    position: absolute;
    left: 353px;
    top: 117px;
    width: 3px;
    height: 236px;
    background: linear-gradient(to bottom, rgba(201,201,201,0), var(--divider) 20%, var(--divider) 80%, rgba(201,201,201,0));
  }
  .agent-name {
    position: absolute;
    left: 398px;
    top: 134px;
    color: var(--honey);
    font-weight: 700;
    font-size: 29px;
    letter-spacing: 0.3px;
  }
  .contact-list {
    position: absolute;
    left: 406px;
    top: 198px;
    list-style: none;
  }
  .contact-list li {
    display: flex;
    align-items: center;
    height: 26.5px;
    font-size: 19px;
    color: var(--ink);
  }
  .contact-list svg { width: 18px; height: 18px; margin-right: 11px; flex: none; }
  .band-line {
    position: absolute; left: 0; right: 0; top: 451px; height: 3px; background: var(--card-black);
  }
  .band-honey {
    position: absolute; left: 0; right: 0; top: 456px; bottom: 0; background: var(--honey);
  }

  /* Back */
  .badges {
    position: absolute;
    top: 34px;
    right: 39px;
    display: flex;
    gap: 24px;
  }
  .badge { width: 46px; height: 45px; background: var(--card-white); }
  .badge--square { width: 40px; height: 45px; }
  .back-mark {
    position: absolute;
    left: 0; right: 0;
    top: 205px;
    text-align: center;
    color: var(--honey);
    font-family: "Roboto", Arial, sans-serif;
    font-weight: 700;
    font-size: 44px;
    letter-spacing: 2px;
  }
  .tagline {
    position: absolute;
    left: 0; right: 0;
    top: 405px;
    text-align: center;
    color: var(--card-white);
    font-family: "Raleway", Arial, sans-serif;
    font-weight: 400;
    font-size: 21px;
  }
</style>
</head>
<body>

  <section class="card card--front">
    <div class="company-mark">Corvane<br>Real Estate</div>

    <div class="team-mark">
      <span class="team-mark__name">LARKSPUR</span>
      <span class="team-mark__sub">REALTY GROUP</span>
    </div>

    <div class="divider"></div>

    <h1 class="agent-name">DYLAN MARSH</h1>

    <ul class="contact-list">
      <li>
        <svg viewBox="0 0 24 24" aria-hidden="true"><path fill="#f7c600" d="M6.6 10.8a15.1 15.1 0 0 0 6.6 6.6l2.2-2.2c.3-.3.7-.4 1-.2 1.1.4 2.3.6 3.6.6.6 0 1 .4 1 1V20c0 .6-.4 1-1 1A17 17 0 0 1 3 4c0-.6.4-1 1-1h3.5c.6 0 1 .4 1 1 0 1.3.2 2.5.6 3.6.1.3 0 .7-.2 1z"/></svg>
        801-555-0172
      </li>
      <li>
        <svg viewBox="0 0 24 24" aria-hidden="true"><rect x="2" y="5" width="20" height="14" fill="#f7c600"/><path d="M2 5l10 8 10-8" fill="none" stroke="#fff" stroke-width="1.8"/></svg>
        dylan@larkspurrealtrygroup.com
      </li>
      <li>
        <svg viewBox="0 0 24 24" aria-hidden="true"><circle cx="12" cy="12" r="10" fill="#f7c600"/><ellipse cx="12" cy="12" rx="4" ry="10" fill="none" stroke="#fff" stroke-width="1.4"/><path d="M2 12h20" stroke="#fff" stroke-width="1.4"/></svg>
        www.larkspurrealtygroup.com
      </li>
      <li>
        <svg viewBox="0 0 24 24" aria-hidden="true"><circle cx="12" cy="12" r="7" fill="#f7c600"/></svg>
        fb/me/larkspurrealtygroup
      </li>
      <li>
        <svg viewBox="0 0 24 24" aria-hidden="true"><circle cx="12" cy="12" r="7" fill="#f7c600"/></svg>
        @LarkspurRltyGrp
      </li>
    </ul>

    <div class="band-line"></div>
    <div class="band-honey"></div>
  </section>

  <section class="card card--back">
    <div class="badges">
      <div class="badge" role="img" aria-label="Housing compliance badge"></div>
      <div class="badge badge--square" role="img" aria-label="Industry membership badge"></div>
    </div>

    <div class="back-mark">Larkspur Realty Group</div>

    <p class="tagline">find out what all the buzz is about</p>
  </section>

</body>
</html>
```